Plakat-Design für LD & Kapitän Funkel
Zielgruppe
Musikformation
Folkrockgeigerin trifft Liedermacher
Eisenkrugpublikum Schnittmenge Valentin Heuberg
Aufgabenstellung
Unteres Drittel darf nicht mit Text bedruckt sein, da dort der Veranstalter Datum und Location draufklebt
zu verarbeitender Text:
Lena Dorothea & Kapitän Funkel
Folkrockgeigerin (bekannt von Eisenkrug (Eisenkrug bitte in bremen bold)) trifft Liedermacher
brandneues Programm: Gläserne Wolken
Es sollen A3 und A4 Poster hochkant werden, leider gibt´s nur querformat Fotos...

```html
<!DOCTYPE html>
<html lang="de">
<head>
<meta charset="utf-8">
<title>Lena Dorothea &amp; Kapitän Funkel – Gläserne Wolken</title>
<link rel="stylesheet" href="https://fonts.googleapis.com/css2?family=Bebas+Neue&family=Great+Vibes&display=swap">
<style>
  :root {
    --page: #ffffff;
    --paper: #ffffff;
    --gold-dark: #8a6a2a;
    --gold-light: #e8cf8a;
    --ink-light: #ffffff;
    --photo-wood: #7a4a32;
    --photo-stone: #a89a86;
    --photo-red: #8c2a22;
    --photo-dark: #3a2a22;
  }
  * { box-sizing: border-box; margin: 0; padding: 0; }
  html, body {
    width: 887px; height: 1200px; overflow: hidden;
    background: var(--page);
  }
  .poster {
    position: absolute;
    left: 66px; top: 60px;
    width: 757px; height: 1074px;
    background: var(--paper);
    box-shadow: 0 4px 14px rgba(0,0,0,0.18);
  }
  .gold-bar {
    position: absolute; left: 0; right: 0; height: 7px;
    background: linear-gradient(90deg, var(--gold-dark), var(--gold-light) 30%, var(--gold-dark) 55%, var(--gold-light) 80%, var(--gold-dark));
  }
  .gold-bar--top { top: 0; }
  .gold-bar--bottom { bottom: 0; }
  .hero {
    position: absolute; left: 0; top: 7px;
    width: 757px; height: 719px;
    overflow: hidden;
  }
  .hero-photo {
    position: absolute; inset: 0;
    background:
      radial-gradient(ellipse at 25% 40%, rgba(190,150,120,0.55), transparent 45%),
      radial-gradient(ellipse at 78% 35%, rgba(180,40,30,0.55), transparent 30%),
      linear-gradient(90deg, var(--photo-wood) 0%, #8a5a3c 30%, var(--photo-stone) 55%, #b8ab96 100%);
  }
  .hero-photo::after {
    content: ""; position: absolute; left: 0; right: 0; bottom: 0; height: 45%;
    background: linear-gradient(180deg, transparent, rgba(58,42,34,0.55) 40%, var(--photo-red) 100%);
    opacity: 0.8;
  }
  .hero-text {
    position: absolute; inset: 0;
    color: var(--ink-light);
    text-align: center;
    font-family: "Bebas Neue", sans-serif;
    text-shadow: 0 1px 3px rgba(0,0,0,0.45);
  }
  .tagline {
    position: absolute; top: 17px; left: 0; right: 0;
    font-size: 17px; letter-spacing: 0.6px;
  }
  .band-name { font-size: 19px; }
  .stars {
    position: absolute; left: 0; right: 0;
    font-size: 19px; letter-spacing: 2px;
    font-family: sans-serif;
  }
  .stars--top { top: 40px; }
  .stars--mid { top: 376px; }
  .program-label {
    position: absolute; top: 418px; left: 0; right: 0;
    font-size: 26px; letter-spacing: 0.5px;
  }
  .program-title {
    position: absolute; top: 440px; left: 0; right: 0;
    font-family: "Great Vibes", cursive;
    font-size: 52px;
  }
  .act-names {
    position: absolute; top: 520px; left: 0; right: 0;
    font-size: 98px; line-height: 94px; letter-spacing: 1px;
  }
</style>
</head>
<body>
  <main class="poster">
    <div class="gold-bar gold-bar--top"></div>
    <section class="hero">
      <div class="hero-photo" role="img" aria-label="Foto: Geigerin und Liedermacher in Trachtenjacke sitzen mit Drehleier, Mandoline und Geigen vor einer alten Holztür und Steinmauer"></div>
      <div class="hero-text">
        <p class="tagline">Folkrockgeigerin (bekannt von <span class="band-name">Eisenkrug</span>) trifft Liedermacher</p>
        <p class="stars stars--top">★★★</p>
        <p class="stars stars--mid">★★★</p>
        <p class="program-label">Brandneues Programm</p>
        <p class="program-title">Gläserne Wolken</p>
        <h1 class="act-names">Lena Dorothea<br>&amp; Kapitän Funkel</h1>
      </div>
    </section>
    <div class="gold-bar gold-bar--bottom"></div>
  </main>
</body>
</html>
```